Elderberry syrup- company product label for placement in grocery chain

I need a label for my elderberry syrup. Trying to decide if I want a logo for each individual product or If I want a label that can be edited from Elderberry Syrup to Elderberry gummies, Elderberry Jam, Etc. I will also need to be able to edit it to different sizes (8oz, 16oz) and edit the ingredients from Honey to Maple Syrup, etc.and remove statements such as "not safe for children under 1" on products that are safe.
I have a couple of competitors in my area. I have included the link to one here: https://www.brambleknollsyrup.com/our-syrup/
And attached a copy of the label of another. I need to have a front and back label or a wrap around label with all the information.

Front: Logo, Elderberry Syrup, 8 fl oz/236 ml, Organic Ingredients, Local honey, Cold-Flu-Allergies, Natural Remedy, Hand Crafted

Back: Ingredients (Organic Elderberries, water, Organic cinnamon, Organic Clove, Organic Ginger, L-ascorbic acid (vit C), Honey

Suggested Use:
Children: 1 tsp (or teaspoon)
Adults: 1 tbsp. (or tablespoon)
preventative: Once daily
When sick: every 3 hours

Other info optional where on labels: Pellham, NC
Refrigerate after opening
Made in NC by Hollow Creek Tonics, LLC
www.hctelderberry.com

*Not safe for children under age 1
*This statement has not been evaluated by the FDA

Barcode

* The bottles used are glass amber bottles.
Possible label ideas are 'kraft' look label, white label, vintage looking label, apothecary looking label. This is a holistic/naturalistic product and the label needs to reflect that.

* I attached my current label as reference for the professional but not commercial look, although my current label is far from professional.

*Logo does not have to be in color. Label can be in black/kraft colors if need be. (Example: bramble knoll syrup label)

Target Market(s)

Holistic/naturalistic crowd

Font styles to use
Sans Serif
Other font styles liked:
• Antipasto to match logo

Colors

Designer to choose colors to be used in the design.

Requirements
Nice to have
• A professional but not commercial look. This is a handcrafted item.

```html
<!DOCTYPE html>
<html lang="en">
<head>
<meta charset="utf-8">
<title>Elderberry Syrup Label</title>
<link rel="stylesheet" href="https://fonts.googleapis.com/css2?family=Barlow:wght@600;700&family=Macondo&display=swap">
<style>
  :root {
    --page-bg: #ffffff;
    --parchment-light: #ddd09a;
    --parchment-mid: #cdbb7c;
    --parchment-dark: #b8a263;
    --berry-purple: #5b2a86;
    --size-purple: #4b2b68;
    --slate-text: #5d6b7c;
    --hairline: #2a2418;
    --sprig-tone: #8f8c6c;
  }
  html, body {
    margin: 0;
    padding: 0;
    width: 1200px;
    height: 1119px;
    overflow: hidden;
    background: var(--page-bg);
  }
  .label-canvas {
    display: block;
    width: 1200px;
    height: 1119px;
  }
  .arc-text {
    font-family: "Barlow", sans-serif;
    font-weight: 600;
    font-size: 18px;
    letter-spacing: 1.2px;
    fill: var(--slate-text);
  }
  .brand-name {
    font-family: "Barlow", sans-serif;
    font-weight: 600;
    font-size: 12px;
    letter-spacing: 2px;
    fill: var(--berry-purple);
  }
  .product-name {
    font-family: "Macondo", cursive;
    font-size: 66px;
    fill: var(--berry-purple);
  }
  .product-size {
    font-family: "Barlow", sans-serif;
    font-weight: 700;
    font-size: 29px;
    fill: var(--size-purple);
  }
</style>
</head>
<body>
<svg class="label-canvas" viewBox="0 0 1100 1025" xmlns="http://www.w3.org/2000/svg">
  <defs>
    <radialGradient id="parchment" cx="45%" cy="40%" r="70%">
      <stop offset="0" stop-color="var(--parchment-light)"/>
      <stop offset="0.6" stop-color="var(--parchment-mid)"/>
      <stop offset="1" stop-color="var(--parchment-dark)"/>
    </radialGradient>
    <radialGradient id="sprig-wash" cx="50%" cy="50%" r="50%">
      <stop offset="0" stop-color="var(--sprig-tone)" stop-opacity="0.45"/>
      <stop offset="1" stop-color="var(--sprig-tone)" stop-opacity="0"/>
    </radialGradient>
    <filter id="label-shadow" x="-10%" y="-10%" width="120%" height="120%">
      <feDropShadow dx="0" dy="2" stdDeviation="6" flood-color="#000" flood-opacity="0.18"/>
    </filter>
    <path id="arc-top" d="M361,508 A196,196 0 0 1 753,508"/>
    <path id="arc-bottom-left" d="M346,526 A212,212 0 0 0 539,719"/>
    <path id="arc-bottom-right" d="M575,719 A212,212 0 0 0 768,526"/>
  </defs>

  <g class="label">
    <circle class="label-base" cx="557" cy="508" r="244" fill="url(#parchment)" filter="url(#label-shadow)"/>

    <ellipse class="berry-sprig" role="img" aria-label="Faint illustration of an elderberry sprig with berries and leaves"
             cx="515" cy="545" rx="120" ry="150" fill="url(#sprig-wash)"/>

    <circle class="frame-ring" cx="557" cy="508" r="231" fill="none" stroke="var(--berry-purple)" stroke-width="5"/>
    <circle class="frame-hairline" cx="557" cy="508" r="222" fill="none" stroke="var(--hairline)" stroke-width="1"/>

    <text class="arc-text"><textPath href="#arc-top" startOffset="50%" text-anchor="middle">ORGANIC INGREDIENTS</textPath></text>

    <g class="brand-mark">
      <circle cx="557" cy="392" r="9" fill="var(--berry-purple)"/>
      <text class="brand-name" x="557" y="422" text-anchor="middle">HOLLOW CREEK TONICS</text>
    </g>

    <text class="product-name" x="557" y="512" text-anchor="middle">Elderberry</text>
    <text class="product-name" x="557" y="592" text-anchor="middle">Syrup</text>

    <text class="product-size" x="557" y="676" text-anchor="middle">8 fl oz</text>

    <text class="arc-text"><textPath href="#arc-bottom-left" startOffset="50%" text-anchor="middle">NATURAL REMEDY</textPath></text>
    <text class="arc-text"><textPath href="#arc-bottom-right" startOffset="50%" text-anchor="middle">COLD-FLU-ALLERGIES</textPath></text>
  </g>
</svg>
</body>
</html>
```